CloudForge Business Card

I need something that flows with the logo and looks professional but creative. I included the thumbnail file of the photo but will upload the source file once I have it. Colors of business card should flow. I am interested in doing the translucent clear plastic cards as well. My company is called CloudForge in one word and the contact details are below:

Dean Holloway
832-574-2938
www.CloudForgeTx.example
dholloway_47@mailbox.example
Updates

Too much red. I'd rather focus on the blue and put some silver or grey in there.

New Files uploaded. Like the designs so far and am looking forward to seeing more.

Looking for a whole new direction. Let's forget about the plastic card. Let's focus on the blue more than red. I still haven't seen something that really grabs me.

Industry/Entity Type

Plastic

```html
<!DOCTYPE html>
<html lang="en">
<head>
<meta charset="UTF-8">
<title>CloudForge Business Card</title>
<link rel="stylesheet" href="https://fonts.googleapis.com/css2?family=Exo+2:wght@500;700&display=swap">
<style>
  :root {
    --backdrop: #d9d9db;
    --card: #f4f4f5;
    --navy: #1f3c86;
    --red: #c8202c;
    --blue-light: #6cb8e6;
    --blue-mid: #2f8fcf;
    --blue-deep: #1a6fb0;
    --grey-text: #6b7280;
    --white: #ffffff;
  }
  * { box-sizing: border-box; margin: 0; padding: 0; }
  html, body {
    width: 1200px; height: 750px; overflow: hidden;
    background: var(--backdrop);
    font-family: "Exo 2", sans-serif;
  }
  .stage { position: relative; width: 1200px; height: 750px; }
  .card {
    position: absolute; top: 232px;
    width: 500px; height: 286px;
    border-radius: 28px;
    background: var(--card);
    overflow: hidden;
    box-shadow: 0 6px 18px rgba(0,0,0,0.12);
  }
  .card--back { left: 70px; }
  .card--front { left: 630px; }

  /* back */
  .back-brand {
    position: absolute; left: 0; right: 0; top: 104px;
    display: flex; align-items: center; justify-content: center; gap: 14px;
  }
  .back-brand__dot {
    width: 30px; height: 30px; border-radius: 50%;
    background: var(--navy);
  }
  .back-brand__name {
    font-weight: 700; font-size: 46px; color: var(--navy); letter-spacing: -0.5px;
  }
  .back-url {
    position: absolute; left: 0; right: 0; top: 182px;
    text-align: center; font-weight: 700; font-size: 19px; color: var(--blue-deep);
  }

  /* front */
  .front-wave { position: absolute; inset: 0; }
  .front-brand {
    position: absolute; left: 38px; top: 70px;
    font-weight: 700; font-size: 44px; color: var(--navy); letter-spacing: -0.5px;
  }
  .front-person { position: absolute; left: 40px; top: 156px; }
  .front-person__name { font-weight: 700; font-size: 17px; color: var(--navy); }
  .front-person__role { font-weight: 500; font-size: 15px; color: var(--grey-text); }
  .contact {
    position: absolute; display: flex; align-items: center; gap: 8px;
    font-weight: 500; font-size: 14px; color: var(--white);
    white-space: nowrap;
  }
  .contact--phone { left: 40px; top: 246px; }
  .contact--email { left: 238px; top: 244px; }
  .contact__icon { width: 20px; height: 20px; flex: none; }
</style>
</head>
<body>
<main class="stage">

  <section class="card card--back" aria-label="Card back">
    <div class="back-brand">
      <span class="back-brand__dot"></span>
      <span class="back-brand__name">CloudForge</span>
    </div>
    <p class="back-url">www.CloudForgeTx.example</p>
  </section>

  <section class="card card--front" aria-label="Card front">
    <svg class="front-wave" viewBox="0 0 500 286" width="500" height="286" aria-hidden="true">
      <defs>
        <linearGradient id="waveBlue" x1="0" y1="0" x2="1" y2="1">
          <stop offset="0" stop-color="#6cb8e6"/>
          <stop offset="0.5" stop-color="#2f8fcf"/>
          <stop offset="1" stop-color="#1a6fb0"/>
        </linearGradient>
      </defs>
      <path d="M0,238 C150,258 300,246 360,150 C400,88 440,42 500,32 L500,286 L0,286 Z" fill="url(#waveBlue)"/>
      <path d="M0,228 C150,248 292,236 352,140 C392,78 432,32 500,22" fill="none" stroke="#1f3c86" stroke-width="4"/>
      <path d="M0,218 C150,238 284,226 344,130 C384,68 424,22 500,12" fill="none" stroke="#c8202c" stroke-width="4"/>
    </svg>

    <div class="front-brand">CloudForge</div>

    <div class="front-person">
      <p class="front-person__name">Dean Holloway</p>
      <p class="front-person__role">role</p>
    </div>

    <div class="contact contact--phone">
      <svg class="contact__icon" viewBox="0 0 20 20" aria-hidden="true">
        <circle cx="10" cy="10" r="9" fill="none" stroke="#ffffff" stroke-width="1.5"/>
        <path d="M7 5.5 L8.6 7.6 L7.8 8.8 C8.4 10 9.8 11.5 11.2 12.2 L12.4 11.4 L14.5 13 L13.4 14.5 C10 14.3 5.8 10.2 5.6 6.6 Z" fill="#ffffff"/>
      </svg>
      <span>832-574-2938</span>
    </div>

    <div class="contact contact--email">
      <svg class="contact__icon" viewBox="0 0 20 20" aria-hidden="true">
        <circle cx="10" cy="10" r="9.5" fill="#ffffff"/>
        <rect x="5" y="6.5" width="10" height="7" rx="1" fill="none" stroke="#2f8fcf" stroke-width="1.4"/>
        <path d="M5.3 7 L10 10.8 L14.7 7" fill="none" stroke="#2f8fcf" stroke-width="1.4"/>
      </svg>
      <span>dholloway_47@mailbox.example</span>
    </div>
  </section>

</main>
</body>
</html>
```